Professional and creatice Life Coach - Business Card design

I just relaunched my website and now i a need a correspoonding business card for my task as life coach. My website is www.tbalrond.com as reference. The compass is kind of a symbol for my work, as I help people navigate through their challenging phases in life. The business card should be colorful, but not too playful as I also adress business people. So it sould be creative, but professional (also to suport my other business as Management Consultant)

Target Market(s)

People who want to get teir problems resolved, in business, partnership and other personal realms

Industry/Entity Type

Life Coaching

Contact Information for Business Card

Front side should include Name, Phone number, Email, Website and address

Font styles to use
Sans Serif

Colors
add136

Requirements
Must have
• "Mag. Leopold Brantner" -> Name
"Energetische Praxis" -> Jobtitle (describing my profession as life coach)
colours and style should match my website www.tbalrond.com
Nice to have
• a compass as a symbol

```html
<!DOCTYPE html>
<html lang="de">
<head>
<meta charset="utf-8">
<title>Leopold Brantner – Visitenkarte</title>
<link rel="stylesheet" href="https://fonts.googleapis.com/css2?family=Poppins:wght@300;400;500&family=Tinos:wght@700&display=swap">
<style>
  :root {
    --stage: #2b2b2b;
    --paper: #ffffff;
    --lime: #c9e07a;
    --lime-deep: #bcd46c;
    --ink: #1a1a1a;
    --ink-soft: #333333;
    --rule: #4a4a4a;
    --mist: #e6e6e6;
  }
  * { box-sizing: border-box; margin: 0; padding: 0; }
  html, body {
    width: 1200px; height: 900px; overflow: hidden;
    background: var(--stage);
  }
  .stage {
    width: 1200px; height: 900px;
    display: flex; flex-direction: column; align-items: center; justify-content: center;
    gap: 40px;
  }
  .card {
    position: relative;
    width: 660px; height: 380px;
    overflow: hidden;
    box-shadow: 0 10px 30px rgba(0,0,0,.45);
  }

  /* Front */
  .card--front { background: var(--paper); color: var(--ink); }
  .front__accent {
    position: absolute; right: -150px; top: 110px;
    width: 300px; height: 300px; border-radius: 50%;
    background: var(--mist);
  }
  .brand {
    position: absolute; left: 150px; top: 52px;
    display: flex; align-items: center; gap: 10px;
  }
  .brand__dot {
    width: 44px; height: 44px; border-radius: 50%;
    background: var(--ink);
  }
  .brand__name {
    font-family: 'Poppins', sans-serif; font-weight: 500;
    font-size: 15px; letter-spacing: 3px; color: var(--ink);
  }
  .identity {
    position: absolute; left: 300px; top: 108px;
  }
  .identity__name {
    font-family: 'Tinos', serif; font-weight: 700;
    font-size: 25px; letter-spacing: .5px; color: var(--ink);
  }
  .identity__title {
    font-family: 'Poppins', sans-serif; font-weight: 300;
    font-size: 16px; color: var(--ink-soft); margin-top: 2px;
  }
  .front__rule {
    position: absolute; left: 90px; right: 60px; top: 192px;
    height: 1px; background: var(--rule);
  }
  .contacts {
    position: absolute; left: 60px; top: 206px;
    list-style: none;
    font-family: 'Poppins', sans-serif; font-weight: 400;
    font-size: 14px; line-height: 26px; color: var(--ink);
  }
  .contacts li { display: flex; align-items: center; gap: 10px; }
  .contacts svg { width: 13px; height: 13px; fill: var(--ink); flex: none; }
  .address {
    position: absolute; right: 60px; bottom: 46px;
    text-align: right;
    font-family: 'Poppins', sans-serif; font-weight: 400;
    font-size: 15px; line-height: 24px; color: var(--ink);
  }

  /* Back */
  .card--back { background: var(--lime); }
  .back__pattern {
    position: absolute; inset: 0;
    background: radial-gradient(circle at 55% 42%, var(--lime-deep) 0%, var(--lime) 70%);
  }
  .back__brand {
    position: absolute; left: 0; right: 0; top: 120px;
    display: flex; align-items: center; justify-content: center; gap: 16px;
  }
  .back__brand .brand__dot { width: 70px; height: 70px; }
  .back__brand .brand__name { font-size: 26px; letter-spacing: 6px; }
  .back__url {
    position: absolute; left: 0; right: 0; bottom: 70px;
    text-align: center;
    font-family: 'Poppins', sans-serif; font-weight: 400;
    font-size: 15px; letter-spacing: 6px; color: var(--ink);
  }
</style>
</head>
<body>
<main class="stage">

  <section class="card card--front" aria-label="Vorderseite">
    <div class="front__accent"></div>
    <div class="brand">
      <span class="brand__dot"></span>
      <span class="brand__name">BRANTNER</span>
    </div>
    <div class="identity">
      <h1 class="identity__name">Mag. Leopold Brantner</h1>
      <p class="identity__title">Energetische Praxis</p>
    </div>
    <div class="front__rule"></div>
    <ul class="contacts">
      <li>
        <svg viewBox="0 0 24 24" aria-hidden="true"><path d="M6.6 10.8a15.1 15.1 0 0 0 6.6 6.6l2.2-2.2a1 1 0 0 1 1-.25 11.4 11.4 0 0 0 3.6.57 1 1 0 0 1 1 1V20a1 1 0 0 1-1 1A17 17 0 0 1 3 4a1 1 0 0 1 1-1h3.5a1 1 0 0 1 1 1c0 1.25.2 2.45.57 3.57a1 1 0 0 1-.25 1z"/></svg>
        +43 660 4817392
      </li>
      <li>
        <svg viewBox="0 0 24 24" aria-hidden="true"><path d="M2 5h20v14H2z M4 7v.4l8 5.3 8-5.3V7z" fill-rule="evenodd"/></svg>
        leopold@brantner.one
      </li>
      <li>
        <svg viewBox="0 0 24 24" aria-hidden="true"><path d="M12 2a10 10 0 1 0 0 20 10 10 0 0 0 0-20zm6.9 6h-2.9a15 15 0 0 0-1.4-3.6A8 8 0 0 1 18.9 8zM12 4c.8 1.2 1.5 2.5 1.9 4h-3.8c.4-1.5 1.1-2.8 1.9-4zM4.3 14a8 8 0 0 1 0-4h3.3a16 16 0 0 0 0 4zm.8 2h2.9c.3 1.3.8 2.5 1.4 3.6A8 8 0 0 1 5.1 16zM8 8H5.1a8 8 0 0 1 4.3-3.6C8.8 5.5 8.3 6.7 8 8zm4 12c-.8-1.2-1.5-2.5-1.9-4h3.8c-.4 1.5-1.1 2.8-1.9 4zm2.3-6H9.7a14.7 14.7 0 0 1 0-4h4.6a14.7 14.7 0 0 1 0 4zm.3 5.6c.6-1.1 1.1-2.3 1.4-3.6h2.9a8 8 0 0 1-4.3 3.6zM16.4 14a16 16 0 0 0 0-4h3.3a8 8 0 0 1 0 4z"/></svg>
        www.tbalrond.com
      </li>
    </ul>
    <address class="address">
      Birkenweg 12, 5071 Wals<br>Österreich
    </address>
  </section>

  <section class="card card--back" aria-label="Rückseite">
    <div class="back__pattern" role="img" aria-label="Faint tone-on-tone compass pattern background"></div>
    <div class="back__brand">
      <span class="brand__dot"></span>
      <span class="brand__name">BRANTNER</span>
    </div>
    <p class="back__url">WWW.TBALROND.COM</p>
  </section>

</main>
</body>
</html>
```